Graphic Design Project

i need Demo graphics designed for my Restaurant App. The app name "TableLoop Plus".
This a Demo app to show potential restaurant owners to try to get them to buy. With the app you can view restaurant men us, specials and events. Post Fanwall and reviews. Alot of other options.
I need the main screen and icons created with the TableLoop Plus logo created. I also need the Specials page created that i will use for the events page also. Also need the reviews page created that i will use for the fanwall page also.
I also need a menu page designed and to match the theme.
I uploaded a few sample screenshots of the current app design.
Updates

Payment is now Guarantee.

Project Deadline Extended
Reason: Need more time for submissions

Hi Do you plan on submitting an updated design soon?

Target Market(s)

restaurant owners. trying to sell them the app.

Industry/Entity Type

Restaurant

Requirements
Must have
• background of something nice that represent a a restaurant but not specific to any one type pf food. Maybe like spoon and fork design or something.
Nice to have
• different icons that represent the different buttons.
eye catching design.
ease of use buttons.

```html
<!DOCTYPE html>
<html lang="en">
<head>
<meta charset="utf-8">
<title>TableLoop Plus – Main Screen</title>
<link href="https://fonts.googleapis.com/css2?family=Questrial&display=swap" rel="stylesheet">
<style>
  :root {
    --stage: #3f3f3f;
    --screen-dark: #0d0d0d;
    --napkin-red: #b3121c;
    --napkin-deep: #5a070c;
    --orange-light: #f9a230;
    --orange-dark: #ea7200;
    --tile-dark-top: #3a3a3a;
    --tile-dark-bottom: #0e0e0e;
    --tile-edge: #8a1a1f;
    --ink: #ffffff;
    --icon-cut: #222222;
  }
  * { box-sizing: border-box; margin: 0; padding: 0; }
  html, body { width: 1200px; height: 830px; overflow: hidden; }
  body {
    background: var(--stage);
    font-family: "Questrial", "Century Gothic", sans-serif;
    color: var(--ink);
    position: relative;
  }
  .app-screen {
    position: absolute;
    left: 330px; top: 25px;
    width: 540px; height: 780px;
    overflow: hidden;
    background: var(--screen-dark);
  }
  .table-setting-photo {
    position: absolute; inset: 0;
    background:
      radial-gradient(ellipse 60% 40% at 70% 78%, rgba(210,210,210,.55), transparent 70%),
      linear-gradient(160deg, #050505 0%, #1a1a1a 28%, var(--napkin-deep) 40%, var(--napkin-red) 52%, #e8e8e8 60%, var(--napkin-red) 68%, var(--napkin-deep) 78%, #111 92%);
  }
  .brand {
    position: absolute; left: 30px; top: 30px;
  }
  .brand-name {
    font-size: 56px; line-height: 1; letter-spacing: -0.5px;
    color: var(--ink);
    white-space: nowrap;
  }
  .tile-board {
    position: absolute; left: 28px; top: 112px;
    width: 356px; height: 628px;
    display: flex; gap: 6px;
  }
  .primary-tiles, .secondary-tiles {
    display: flex; flex-direction: column; gap: 4px;
  }
  .primary-tiles { width: 210px; }
  .secondary-tiles { width: 140px; }
  .tile {
    position: relative; flex: 1;
    display: flex; align-items: center; justify-content: center;
  }
  .tile-primary {
    background: linear-gradient(180deg, var(--orange-light), var(--orange-dark));
  }
  .tile-secondary {
    background: linear-gradient(180deg, var(--tile-dark-top), var(--tile-dark-bottom));
    border-bottom: 2px solid var(--tile-edge);
    justify-content: flex-start; padding-left: 22px;
  }
  .tile svg { fill: var(--ink); display: block; }
  .tile-primary svg { width: 118px; height: 88px; margin-top: -22px; }
  .tile-secondary svg { width: 60px; height: 56px; margin-top: -18px; }
  .tile-label {
    position: absolute; right: 8px; bottom: 6px;
    text-transform: uppercase; line-height: 1;
    white-space: nowrap;
  }
  .tile-primary .tile-label { font-size: 21px; }
  .tile-secondary .tile-label { font-size: 15px; }
</style>
</head>
<body>
  <main class="app-screen">
    <div class="table-setting-photo" role="img" aria-label="Photo of a plate with fork and knife on a red napkin"></div>

    <header class="brand">
      <span class="brand-name">TableLoop Plus</span>
    </header>

    <nav class="tile-board">
      <div class="primary-tiles">
        <a class="tile tile-primary">
          <svg viewBox="0 0 118 88"><path d="M4 10 Q30 2 56 12 V84 Q30 74 4 82 Z M62 12 Q88 2 114 10 V82 Q88 74 62 84 Z"/></svg>
          <span class="tile-label">Menu</span>
        </a>
        <a class="tile tile-primary">
          <svg viewBox="0 0 118 88"><polygon points="58,2 70,32 102,32 76,52 86,84 58,64 30,84 40,52 14,32 46,32"/><polygon points="14,64 17,71 24,71 18,75 20,82 14,78 8,82 10,75 4,71 11,71"/><polygon points="104,60 107,67 114,67 108,71 110,78 104,74 98,78 100,71 94,67 101,67"/></svg>
          <span class="tile-label">Specials</span>
        </a>
        <a class="tile tile-primary">
          <svg viewBox="0 0 118 88"><polygon points="59,2 74,18 44,18"/><polygon points="59,86 74,70 44,70"/><polygon points="14,44 32,28 32,60"/><polygon points="104,44 86,28 86,60"/><path d="M44 30h8v4h-4v4h-4z M74 30h-8v4h4v4h4z M44 58h8v-4h-4v-4h-4z M74 58h-8v-4h4v-4h4z M53 38h12v12H53z"/></svg>
          <span class="tile-label">Directions</span>
        </a>
        <a class="tile tile-primary">
          <svg viewBox="0 0 118 88"><rect x="14" y="8" width="90" height="74" rx="4"/><path d="M30 4v12M50 4v12M70 4v12M90 4v12" stroke="#fff" stroke-width="6"/><path d="M50 34h26l-14 40h-10l13-31H50z" fill="#e87400"/></svg>
          <span class="tile-label">Events</span>
        </a>
      </div>
      <div class="secondary-tiles">
        <a class="tile tile-secondary">
          <svg viewBox="0 0 60 56"><circle cx="28" cy="30" r="24" fill="none" stroke="#fff" stroke-width="4"/><path d="M28 30 V6 A24 24 0 0 1 52 30 Z"/><path d="M28 30 L52 30 A24 24 0 0 1 40 51 Z"/></svg>
          <span class="tile-label">Polls</span>
        </a>
        <a class="tile tile-secondary">
          <svg viewBox="0 0 60 56"><rect x="6" y="4" width="36" height="48" rx="2"/><path d="M12 14h24M12 22h24M12 30h24M12 38h16" stroke="#222" stroke-width="3"/><path d="M48 10 l6 2 -8 38 -6 -2z"/></svg>
          <span class="tile-label">Reviews</span>
        </a>
        <a class="tile tile-secondary">
          <svg viewBox="0 0 60 56"><rect x="10" y="6" width="44" height="44"/></svg>
          <span class="tile-label">Circlefeed</span>
        </a>
        <a class="tile tile-secondary">
          <svg viewBox="0 0 60 56"><path d="M2 6h40v22H20l-10 8v-8H2z"/><path d="M30 30h28v16h-6v6l-8-6H30z"/></svg>
          <span class="tile-label">Fanwall</span>
        </a>
        <a class="tile tile-secondary">
          <svg viewBox="0 0 60 56"><path d="M4 16h12l5-7h18l5 7h12v34H4z"/><circle cx="30" cy="32" r="12" fill="#222"/><circle cx="30" cy="32" r="7"/></svg>
          <span class="tile-label">Gallery</span>
        </a>
        <a class="tile tile-secondary">
          <svg viewBox="0 0 60 56"><circle cx="30" cy="28" r="26"/><path d="M24 12h12v10h10v12H36v10H24V34H14V22h10z" fill="#222"/></svg>
          <span class="tile-label">More...</span>
        </a>
      </div>
    </nav>
  </main>
</body>
</html>
```